Vision / Mission Poster Required

We are looking to display our company Vision / Mission / Values on a poster. This will be displayed in the head office and other site offices.

The document needs to look professional however still be fun, eye catching and easy to read. It will be predominantly displayed in A3 format.

The design needs to use our company Logo which is attached along with the Text to display on the poster. I have put some additional text on the doc that you can include if it suits the layout but is not essential.

Target Market(s)

Staff, Corporate Visitors

Industry/Entity Type

Electric Company

Font styles to use
Sans Serif

Colors

Designer to choose colors to be used in the design.

Requirements
Must have
• Incorporate Logo
• Professional Look
• Attention grabbing
• Easy to Read
Should not have
• Lightning Bolts
• Pictures of random people/Things

```html
<!DOCTYPE html>
<html lang="en">
<head>
<meta charset="utf-8">
<title>Keystone Electrical – Vision, Mission &amp; Values</title>
<link rel="stylesheet" href="https://fonts.googleapis.com/css2?family=Open+Sans:wght@400;600;700&display=swap">
<style>
  :root {
    --navy: #1f3a6e;
    --blue: #2f5fe0;
    --orange: #f58a2c;
    --orange-light: #f9a55a;
    --peach: #fbc196;
    --text: #3a3f4a;
    --white: #ffffff;
  }
  * { box-sizing: border-box; margin: 0; padding: 0; }
  html, body { width: 951px; height: 1200px; overflow: hidden; background: var(--white); }
  body { font-family: "Open Sans", Arial, sans-serif; color: var(--navy); }
  .poster { position: relative; width: 951px; height: 1200px; overflow: hidden; background: var(--white); }
  .hero { position: absolute; top: 0; left: 0; width: 951px; height: 560px; }

  .brand { position: absolute; left: 582px; top: 440px; display: flex; align-items: center; gap: 14px; }
  .brand-dot { width: 52px; height: 52px; border-radius: 50%; background: var(--orange); }
  .brand-name { font-size: 36px; font-weight: 700; line-height: 1.02; color: var(--navy); letter-spacing: 0.5px; }

  .pill {
    display: inline-block; padding: 2px 34px 4px; border-radius: 20px;
    background: linear-gradient(180deg, var(--orange-light), var(--orange));
    color: var(--white); font-weight: 400; font-size: 26px; line-height: 1.3;
    box-shadow: 0 3px 5px rgba(0,0,0,0.18);
  }

  .values { position: absolute; left: 61px; top: 565px; width: 410px; height: 557px;
    background: var(--peach); border-radius: 18px; padding: 34px 24px 0; text-align: center; }
  .values-title { position: absolute; top: -28px; left: 50%; transform: translateX(-50%); font-size: 30px; padding: 0 42px 4px; }
  .value { margin-bottom: 12px; }
  .value-num { display: inline-flex; align-items: center; justify-content: center; width: 20px; height: 20px;
    border-radius: 50%; background: var(--navy); color: var(--white); font-size: 12px; font-weight: 700; }
  .value-title { font-size: 16px; font-weight: 700; color: var(--navy); margin: 2px 0 3px; }
  .value-text { font-size: 11.5px; line-height: 1.4; color: var(--text); }

  .column { position: absolute; left: 560px; width: 310px; text-align: center; }
  .vision { top: 578px; }
  .vision .pill { font-size: 24px; padding: 0 44px 2px; }
  .vision-line { margin-top: 14px; font-size: 27px; font-weight: 700; line-height: 1.4; color: var(--navy); }

  .mission { top: 738px; }
  .mission .pill { font-size: 28px; padding: 0 36px 3px; position: relative; z-index: 1; }
  .mission-track { position: absolute; left: 50%; top: 36px; width: 2px; height: 260px; background: var(--orange); transform: translateX(-1px); }
  .goal { position: relative; z-index: 1; margin-top: 20px; }
  .goal:first-of-type { margin-top: 22px; }
  .goal-head { display: inline-block; background: var(--white); border: 2px solid var(--orange);
    color: var(--orange); font-size: 15px; font-weight: 700; padding: 1px 12px; min-width: 232px; }
  .goal-text { background: var(--white); margin-top: 8px; font-size: 11px; font-weight: 600; line-height: 1.45; color: var(--navy); }
  .goal + .goal { margin-top: 24px; }

  .corner-band { position: absolute; right: 0; bottom: 68px; width: 951px; height: 120px; }

  .footer { position: absolute; left: 0; bottom: 0; width: 951px; height: 68px; background: var(--navy);
    display: flex; align-items: center; color: var(--white); }
  .footer-cell { display: flex; align-items: center; gap: 14px; padding: 0 30px; font-size: 14px; line-height: 1.5; }
  .footer-cell + .footer-cell { border-left: 1px solid rgba(255,255,255,0.55); }
  .footer-address { padding-left: 54px; width: 335px; }
  .footer-web { width: 232px; flex-direction: column; align-items: flex-start; gap: 2px; }
  .footer-web span { display: flex; align-items: center; gap: 10px; }
  .footer-phone { font-size: 26px; font-weight: 700; gap: 12px; }
  .icon { flex: none; }
</style>
</head>
<body>
<main class="poster">

  <svg class="hero" viewBox="0 0 951 560" aria-hidden="false">
    <defs>
      <linearGradient id="photoTone" x1="0" y1="0" x2="1" y2="0.6">
        <stop offset="0" stop-color="#6f6a5c"/>
        <stop offset="0.35" stop-color="#c9a443"/>
        <stop offset="0.65" stop-color="#e0a85a"/>
        <stop offset="1" stop-color="#4aa7c9"/>
      </linearGradient>
      <linearGradient id="orangeBand" x1="1" y1="0" x2="0" y2="1">
        <stop offset="0" stop-color="#f7912f"/>
        <stop offset="1" stop-color="#f5a459"/>
      </linearGradient>
    </defs>
    <path role="img" aria-label="Photograph of a lit shopping arcade with a colourful painted mural wall"
          d="M0 0 H900 C780 220 520 380 0 500 Z" fill="url(#photoTone)"/>
    <path class="swoosh-blue" d="M900 0 H951 V60 C800 300 500 425 0 518 V500 C520 380 780 220 900 0 Z" fill="var(--blue)"/>
    <path class="swoosh-orange" d="M951 165 C820 320 520 445 140 505 C520 480 830 410 951 335 Z" fill="url(#orangeBand)"/>
    <path class="tail-blue" d="M0 528 C110 515 220 505 330 500 C220 512 110 528 0 548 Z" fill="var(--blue)"/>
    <path class="tail-orange" d="M0 552 C110 536 220 522 320 512 C220 530 110 552 0 580 Z" fill="var(--orange)"/>
  </svg>

  <div class="brand">
    <div class="brand-dot"></div>
    <div class="brand-name">KEYSTONE<br>ELECTRICAL</div>
  </div>

  <section class="values">
    <div class="pill values-title">Values</div>
    <div class="value">
      <span class="value-num">1</span>
      <h3 class="value-title">Honesty &amp; Integrity</h3>
      <p class="value-text">Customers, contractors and suppliers will be able to count on Keystone personnel to deal straightforwardly and adhere to the strictest moral and ethical codes of conduct.</p>
    </div>
    <div class="value">
      <span class="value-num">2</span>
      <h3 class="value-title">Safety &amp; Responsibility</h3>
      <p class="value-text">Keystone is committed to constantly improving safety practices at project job sites and within the electrical service industry as a whole.</p>
    </div>
    <div class="value">
      <span class="value-num">3</span>
      <h3 class="value-title">Commitment to Quality</h3>
      <p class="value-text">Customers and stakeholders will be able to count on Keystone's workmanship being among the best in the industry.</p>
    </div>
    <div class="value">
      <span class="value-num">4</span>
      <h3 class="value-title">Innovation &amp; Technology</h3>
      <p class="value-text">Customers can rely on us to apply the latest proven technologies on their projects, and to be on the ground floor of industry standards for new and emerging markets.</p>
    </div>
    <div class="value">
      <span class="value-num">5</span>
      <h3 class="value-title">Knowledgeable &amp; Valued Employees</h3>
      <p class="value-text">Keystone recognizes that its greatest asset is its people. We pledge to treat each employee with integrity, dealing honestly with all.</p>
    </div>
  </section>

  <section class="column vision">
    <div class="pill">Vision</div>
    <p class="vision-line">Dynamic results -<br>Proven reputation</p>
  </section>

  <section class="column mission">
    <div class="mission-track"></div>
    <div class="pill">Mission</div>
    <div class="goal">
      <div class="goal-head">Deliver Growth and Value</div>
      <p class="goal-text">Maintaining a market presence -<br>Leveraging our technical resources –<br>Networking and developing<br>stakeholder relationships</p>
    </div>
    <div class="goal">
      <div class="goal-head">Remain Profitable</div>
      <p class="goal-text">Increasing revenue -<br>Optimizing capacity utilization –<br>Maintaining expenses</p>
    </div>
    <div class="goal">
      <div class="goal-head">Be Sustainable</div>
      <p class="goal-text">Improving internal efficiency –<br>Diversifying our income sources –<br>Implementing Social &amp; Environmental<br>Improvement Initiatives</p>
    </div>
  </section>

  <svg class="corner-band" viewBox="0 0 951 120" aria-hidden="true">
    <path d="M951 0 V120 H870 C900 80 925 40 951 0 Z" fill="var(--navy)"/>
  </svg>

  <footer class="footer">
    <div class="footer-cell footer-address">
      <svg class="icon" width="18" height="18" viewBox="0 0 24 24" fill="none" stroke="#fff" stroke-width="2">
        <circle cx="12" cy="12" r="10"/><path d="M12 17 C9 13 8.5 11.5 8.5 10.5 a3.5 3.5 0 0 1 7 0 C15.5 11.5 15 13 12 17 Z"/>
      </svg>
      <span>14 Harlow St<br>Westbrook WA 6100</span>
    </div>
    <div class="footer-cell footer-web">
      <span>
        <svg class="icon" width="18" height="18" viewBox="0 0 24 24" fill="none" stroke="#fff" stroke-width="2">
          <circle cx="12" cy="12" r="10"/><rect x="7" y="8.5" width="10" height="7"/><path d="M7 8.5 L12 12.5 L17 8.5"/>
        </svg>info@keystonewa.com.au</span>
      <span>
        <svg class="icon" width="18" height="18" viewBox="0 0 24 24" fill="none" stroke="#fff" stroke-width="2">
          <circle cx="12" cy="12" r="10"/><path d="M2 12 H22 M12 2 C8 6 8 18 12 22 M12 2 C16 6 16 18 12 22"/>
        </svg>www.keystonewa.com.au</span>
    </div>
    <div class="footer-cell footer-phone">
      <svg class="icon" width="26" height="26" viewBox="0 0 24 24" fill="none" stroke="#fff" stroke-width="2" stroke-linejoin="round">
        <path d="M5 3 H9 L10.5 8 L8 9.5 C9 12 11.5 14.5 14 15.5 L15.5 13 L20.5 14.5 V18.5 C20.5 19.5 19.5 20.5 18.5 20.5 C10.5 20 4 13.5 3.5 5.5 C3.5 4 4 3 5 3 Z"/>
      </svg>
      <span>08 9000 4821</span>
    </div>
  </footer>

</main>
</body>
</html>
```